Solo consultant in research/analytics/data science space needs new business card

I need a new business card to promote my solo business as creative problem solver and consultant. I work on business projects for sales and market research and analytics, customer/market insights, and data science. I provide clients data-informed insights and ideas to enhance their businesses. My initial tagline: 'Make your data work for YOU.'

People should hire me because of my diverse background. Because of my Ph.D. in Political Science I have a strong background in research and analytics, project design and management, and communications skills. With my experience as a marketing analyst, a volunteer on non-profit projects, and currently as research consultant I have worked on projects within various industries. I also have a taste for improvisation so I enjoy thinking creatively and appreciate design thinking.

As an introduction to my background: Clients might want to hire me for many types of projects. Clients might wish to understand who their best customers are and how to characterize them. Maybe clients want to know how their customers feel about a certain product or service. Clients might want to know more about their local market area and overall industry. Clients might want to know whether their marketing programs are effective or else what drives their sales revenue. Perhaps clients want to use their data to create something useful for themselves or their customers.

One client hired me to help them decide whether to expand their services to newer customers. I gathered and analyzed information about the local area – the characteristics of people living there as well as the client’s competitors – and described trends and implications. The client was very pleased with the results and submitted them to superiors for approval to move forward.

For another client – who was looking to purchase a house in a metropolitan area – I gathered population and school data about the area. With this, I created an interactive mapping tool so they could zoom in on neighborhoods and learn more about them before they selected a neighborhood to purchase a house. They were happy with the results of my work.

When I worked as a marketing analyst for a consulting firm, a Vice President of Marketing hired us to discover whether or not the company’s marketing programs (i.e. coupons and discounts) were effective. I analyzed their data and our team discovered their marketing was indeed effective. He was very happy and used this to justify their programs to the Finance department (who thought such programs lost revenue).

- Marcus Delano Whitby, Ph.D.

Target Market(s)

Future clients and employers. The most immediate target markets will be other service providers such as consulting companies, marketing firms and ad agencies. I will also use this for meeting with clients in various industries.

Industry/Entity Type

Consulting

Contact Information for Business Card

Since it is my first real business card as a solo practitioner, I want to make an excellent first impression. I want this useful in case someone hires me to work on projects or else hire me to work within a firm or company. The card should convey competence and some creativity while also being neither stuffy nor a data geek.

Colors

Designer to choose colors to be used in the design.

Requirements
Nice to have
• Attached are the starting efforts at the card to add some color. It will be nice to use my name and descriptors on one side and tagline on the other. If anyone has better ideas, I will love to see them!

```html
<!DOCTYPE html>
<html lang="en">
<head>
<meta charset="UTF-8">
<title>Marcus Delano Whitby – Business Card</title>
<link href="https://fonts.googleapis.com/css2?family=Lato:wght@300;400;700&family=Tinos:ital@0;1&display=swap" rel="stylesheet">
<style>
  :root {
    --bg: #2a2d31;
    --card: #1a1a1b;
    --accent: #e8573f;
    --text: #f2f2f2;
    --muted: #bdbdbd;
  }
  * { margin: 0; padding: 0; box-sizing: border-box; }
  html, body { width: 1200px; height: 900px; overflow: hidden; background: var(--bg); }
  .canvas { position: relative; width: 1200px; height: 900px; font-family: "Lato", sans-serif; }

  .card {
    position: absolute; width: 520px; height: 297px;
    background: var(--card); border-radius: 18px; overflow: hidden;
    box-shadow: 0 14px 30px rgba(0,0,0,.45);
  }
  .card--front { left: 60px; top: 480px; }
  .card--back { left: 620px; top: 120px; }

  /* Front */
  .front__name {
    position: absolute; left: 28px; top: 28px;
    color: var(--text); font-size: 16px; letter-spacing: .3px; text-transform: uppercase; font-weight: 400;
  }
  .front__role {
    position: absolute; left: 28px; top: 52px; width: 300px;
    color: var(--accent); font-family: "Tinos", serif; font-size: 11.5px; line-height: 1.3;
  }
  .front__rule { position: absolute; left: 28px; top: 96px; width: 400px; height: 1px; background: var(--accent); }
  .contact { position: absolute; left: 28px; top: 110px; list-style: none; }
  .contact li { display: flex; align-items: center; gap: 8px; color: var(--muted); font-size: 11.5px; height: 19px; }
  .contact svg { width: 10px; height: 10px; fill: var(--accent); flex: none; }
  .brand-name {
    position: absolute; right: 28px; top: 140px;
    color: var(--accent); font-size: 20px; font-weight: 400; letter-spacing: .5px;
  }
  .social { position: absolute; right: 28px; bottom: 34px; list-style: none; text-align: right; }
  .social li { display: flex; justify-content: flex-end; align-items: center; gap: 8px; color: var(--text); font-size: 13px; height: 22px; }
  .social svg { width: 11px; height: 11px; flex: none; }
  .front__band { position: absolute; left: 0; bottom: 0; width: 100%; height: 14px; background: var(--accent); }

  /* Back */
  .back__rule { position: absolute; left: 230px; width: 60px; height: 2px; background: var(--accent); }
  .back__rule--top { top: 92px; }
  .back__rule--bottom { top: 203px; }
  .tagline {
    position: absolute; left: 0; right: 0; top: 108px; text-align: center;
    color: var(--text); font-size: 29px; font-weight: 400; line-height: 1.2;
  }
</style>
</head>
<body>
<div class="canvas">

  <section class="card card--back">
    <div class="back__rule back__rule--top"></div>
    <p class="tagline">Make your data<br>work for YOU.</p>
    <div class="back__rule back__rule--bottom"></div>
  </section>

  <section class="card card--front">
    <h1 class="front__name">Marcus Delano Whitby, Ph.D.</h1>
    <p class="front__role">Reasearch/Analytics - Customer Intelligence - Date Science Consultant</p>
    <div class="front__rule"></div>
    <ul class="contact">
      <li><svg viewBox="0 0 10 10"><path d="M5 0a3.5 3.5 0 0 0-3.5 3.5C1.5 6 5 10 5 10s3.5-4 3.5-6.5A3.5 3.5 0 0 0 5 0zm0 5a1.5 1.5 0 1 1 0-3 1.5 1.5 0 0 1 0 3z"/></svg>Lisbon, PT</li>
      <li><svg viewBox="0 0 10 10"><path d="M2 0h2l1 2.5-1.3 1a6 6 0 0 0 2.8 2.8l1-1.3L10 6v2a2 2 0 0 1-2 2C3.6 10 0 6.4 0 2a2 2 0 0 1 2-2z"/></svg>+351 912 604 318</li>
      <li><svg viewBox="0 0 10 10"><path d="M0 2h10v6H0z M0 2l5 3.5L10 2" stroke="#1a1a1b" stroke-width=".8"/></svg>mdwhitby@inboxmail.pt</li>
    </ul>
    <div class="brand-name">Whitby Consulting</div>
    <ul class="social">
      <li>@MDWhitby<svg viewBox="0 0 10 10"><rect width="10" height="10" rx="1.5" fill="var(--accent)"/></svg></li>
      <li>marcusdwhitby.com<svg viewBox="0 0 10 10" fill="none" stroke="var(--accent)" stroke-width="1"><circle cx="5" cy="5" r="4.4"/><path d="M.6 5h8.8M5 .6c-2.4 2.6-2.4 6.2 0 8.8M5 .6c2.4 2.6 2.4 6.2 0 8.8"/></svg></li>
    </ul>
    <div class="front__band"></div>
  </section>

</div>
</body>
</html>
```